Tranquil Harbor yoga, meditation & wellness

I teach kundalini yoga and meditation classes.
I have adult beginner classes, seniors classes, family yoga classes, kids yoga classes
I also offer events like cacao ceremony, full moon ceremony, and retreats

Professional, and simple website that is easy to navigate, and easy for me to update, change.

Target Market(s)

all ages

Industry/Entity Type

Health And Wellness

Coding

Coded - Design and coding required

Number of Pages Required

5+ page

Font styles to use
Decorative

Colors
cedeed
eedded
e4daeb
fbd4d5
fee3d4

Requirements
Must have
• tabs required: about, contact, events, classes, blog,
• I would like to link my facebook page & instagram accounts to the website
Nice to have
• I would like my clients to be able to register for classes and events from my website
• I would like to have a "shop" option in the future, for some items that I have for sale

```html
<!DOCTYPE html>
<html lang="en">
<head>
<meta charset="utf-8">
<title>Tranquil Harbor — Kundalini Yoga</title>
<link rel="stylesheet" href="https://fonts.googleapis.com/css2?family=Poppins:wght@300;400;500;600;700&display=swap">
<style>
:root{
  --blue:#cedeed;
  --blue-soft:#e6eef7;
  --pink:#fbd4d5;
  --peach:#fee3d4;
  --lilac:#e4daeb;
  --lilac-soft:#efe7f4;
  --rose:#eedded;
  --ink:#3a3a3a;
  --body:#5c5c5c;
  --accent:#b58ac8;
  --dark:#2f2f2f;
  --white:#ffffff;
}
*{box-sizing:border-box;margin:0;padding:0}
html,body{width:1200px;height:4186px;overflow:hidden}
body{position:relative;font-family:"Poppins",sans-serif;color:var(--ink);background:var(--white)}
.abs{position:absolute}
.photo{position:absolute}

/* hero */
.hero{left:0;top:0;width:1200px;height:703px;background:linear-gradient(180deg,#6d7f8a 0%,#c9b79a 30%,#8a7564 55%,#2e2a2a 100%)}
.brand{left:94px;top:28px;display:flex;align-items:center;gap:12px;color:var(--white);font-size:24px;font-weight:400}
.brand-dot{width:40px;height:40px;border-radius:50%;background:var(--white);opacity:.85}
.top-icon{top:28px;width:44px;height:44px;border-radius:50%;background:var(--white);display:flex;align-items:center;justify-content:center}
.hero-mark{left:480px;top:53px;width:240px;height:240px;border-radius:50%;background:var(--blue);display:flex;align-items:center;justify-content:center;text-align:center;font-size:28px;font-weight:500;color:#555;line-height:1.2}
.hero-title{left:0;width:1200px;text-align:center;color:var(--white)}
.hero-title .light{position:absolute;left:0;width:1200px;top:333px;font-size:50px;font-weight:300;letter-spacing:9px}
.hero-title .bold{position:absolute;left:0;width:1200px;top:400px;font-size:54px;font-weight:700;letter-spacing:8px}

.portrait{left:441px;top:536px;width:318px;height:329px;background:var(--white);padding:8px;box-shadow:0 6px 16px rgba(0,0,0,.3)}
.portrait .photo{left:8px;top:8px;width:302px;height:313px;background:linear-gradient(180deg,#8e9a6e 0%,#d8bfa8 50%,#6a6a6a 100%)}
.portrait-name{left:8px;top:265px;width:302px;height:56px;background:rgba(40,40,40,.85);color:var(--white);font-size:17px;font-weight:600;text-align:center;line-height:56px}

/* intro */
.feature{top:767px;display:flex;gap:30px}
.feature-icon{width:78px;height:104px;flex:none}
.feature h3{font-size:22px;font-weight:600;margin-top:8px;margin-bottom:6px;color:var(--ink)}
.feature p{font-size:13px;line-height:1.5;color:var(--body);width:240px}

/* section kundalini */
.practice{left:0;top:943px;width:1200px;height:1108px;background:var(--blue-soft)}
.h2{font-size:40px;font-weight:600;color:var(--ink);line-height:1.2}
.copy{font-size:13.5px;line-height:1.75;color:var(--body)}
.btn{display:inline-block;border:2px solid var(--ink);padding:0 22px;height:50px;line-height:46px;font-size:17px;font-weight:600;color:var(--ink);background:transparent}

/* contribute */
.frame{background:var(--white);padding:14px;box-shadow:0 4px 14px rgba(0,0,0,.25)}
.contribute-title{left:790px;top:2106px;width:400px;font-size:38px}
.contribute-copy{left:790px;top:2250px;width:330px;font-size:12px;line-height:1.7}

/* classes */
.classes{left:0;top:2707px;width:1200px;height:641px;background:var(--lilac-soft)}
.classes-copy{left:86px;top:2840px;width:490px;font-size:12.5px;line-height:1.7}
.class-item{left:86px;width:440px;height:74px;border-bottom:1px solid #cbb9d6;display:flex;gap:18px;align-items:flex-start}
.class-item h4{font-size:19px;font-weight:600;color:var(--accent);line-height:1.3}
.class-item span{font-size:16px;color:var(--body)}

/* blog */
.blog{left:0;top:3348px;width:1200px;height:793px;background:linear-gradient(180deg,#ffffff 0%,#f0f0f0 25%,#b9b9b9 60%,#8d8d8d 100%)}
.card{top:3488px;width:327px;height:232px;padding:24px 22px;box-shadow:0 4px 12px rgba(0,0,0,.2)}
.card h5{font-size:19px;font-weight:600;color:#4a3a3a;line-height:1.45}
.card p{font-size:17px;color:#555;margin-top:14px}
.arrow{top:3590px}
.contact{left:390px;top:3724px;width:420px;height:420px;border-radius:50%;background:var(--white)}
.field{left:480px;width:240px;height:32px;border:1px solid #999;font-size:12px;color:#888;padding:7px 10px;background:var(--white)}
.submit{left:480px;top:4060px;width:240px;height:44px;background:#555;color:var(--white);font-size:13px;font-weight:600;text-align:center;line-height:44px;letter-spacing:1px}

.footer{left:0;top:4141px;width:1200px;height:45px;background:var(--blue);display:flex;align-items:center;justify-content:space-between;padding:0 86px;font-size:13px;color:var(--ink)}
.footer nav{display:flex;gap:24px}
</style>
</head>
<body>

<section class="abs hero" role="img" aria-label="Woman standing on a mountain ridge at sunset with hands raised"></section>
<div class="abs brand"><span class="brand-dot"></span>Tranquil Harbor</div>
<div class="abs top-icon" style="left:1016px">
  <svg width="20" height="20" viewBox="0 0 24 24"><path d="M2 3h3l3 12h11l2-8H7" fill="none" stroke="#333" stroke-width="2"/><circle cx="9" cy="19" r="2" fill="#333"/><circle cx="17" cy="19" r="2" fill="#333"/></svg>
</div>
<div class="abs top-icon" style="left:1072px">
  <svg width="18" height="18" viewBox="0 0 24 24"><path d="M3 6h18M3 12h18M3 18h18" stroke="#333" stroke-width="2.5"/></svg>
</div>
<div class="abs hero-mark">Tranquil<br>Harbor</div>
<h1 class="abs hero-title"><span class="light">EXPERIENCE OF</span><span class="bold">KUNDALINI YOGA</span></h1>

<figure class="abs portrait">
  <div class="photo" role="img" aria-label="Portrait of the yoga teacher wearing a headband outdoors"></div>
  <figcaption class="abs portrait-name">MAYA (DEV PREET KAUR)</figcaption>
</figure>

<div class="abs feature" style="left:84px">
  <svg class="feature-icon" viewBox="0 0 78 104"><path d="M0 0h58l20 20v84H0z" fill="var(--pink)"/><circle cx="39" cy="52" r="16" fill="none" stroke="#fff" stroke-width="3"/></svg>
  <div><h3>Kundalini Yoga</h3><p>The Yoga for everyone. Compared to many other types of yoga, Kundalini Yoga is characterized by</p></div>
</div>
<div class="abs feature" style="left:790px">
  <svg class="feature-icon" viewBox="0 0 78 104"><path d="M0 0h58l20 20v84H0z" fill="var(--lilac)"/><circle cx="39" cy="52" r="16" fill="none" stroke="#fff" stroke-width="3"/></svg>
  <div><h3>For your comfort.</h3><p>Wear loose fitted clothing that is comfortable moves with you. You may wish to wear layers as your</p></div>
</div>

<section class="abs practice"></section>
<div class="photo" style="left:0;top:943px;width:502px;height:611px;background:linear-gradient(180deg,#3e5a3a 0%,#9fb0b5 45%,#e8e8ea 75%,#4a3a48 100%)" role="img" aria-label="Teacher in white meditating cross-legged on a rug in the snow among pine trees"></div>
<h2 class="abs h2" style="left:527px;top:1000px">Kundalini Yoga</h2>
<div class="abs copy" style="left:527px;top:1075px;width:600px">
  <p>Kundalini Yoga comes from northern India and has a centuries-long tradition. It was brought to the West by a visiting master in 1969. It is a powerful yoga system that includes not only physical and meditation exercises, but also healing techniques such as Sat Nam Rasayan and yogic massage, nutrition and lifestyle teachings of Ayurveda, and yogic lifestyle. The comprehensive science of Kundalini Yoga also includes Numerology, the large group meditation courses of White Tantric Yoga, the martial arts technique Gatka, and special pregnancy yoga and yoga for childbirth.</p>
  <p style="margin-top:20px">Kundalini Yoga is also called the "Yoga of Awareness". It is ideal for people in the prime of their lives, because it helps to meet the daily demands and challenges actively while staying calm and balanced. The aim of this comprehensive self-training is the harmonization of body, mind and spirit through posture and movement, concentration, focus and meditation, conscious breathing and sound (mantra).</p>
</div>
<div class="photo" style="left:703px;top:1395px;width:497px;height:656px;background:linear-gradient(180deg,#d9dde3 0%,#f3f3f3 40%,#c8c4c4 75%,#8a8f95 100%)" role="img" aria-label="Teacher in a white turban with hands resting open in meditation in a snowy field"></div>
<h2 class="abs h2" style="left:86px;top:1620px">Your Wellbeing.</h2>
<div class="abs copy" style="left:86px;top:1684px;width:570px">
  <p>You are responsible to make me aware of any medical conditions or physical concerns you may have in general and on the day of your class. I will offer guidance and accommodations based on this knowledge. Chairs and props are available to assist you whenever you need them. It is your responsibility to keep yourself safe and injury free.</p>
  <p style="margin-top:20px">Use your own wisdom and knowledge of your body to make adjustments during your practice. This is YOUR practice and is intended to benefit you and address your particular needs. You always have a choice. You decide what's right for you.</p>
</div>
<a class="abs btn" style="left:86px;top:1928px">Register For Classes</a>

<div class="abs frame" style="left:150px;top:2135px;width:520px;height:440px;transform:rotate(5deg)"></div>
<div class="abs frame" style="left:126px;top:2160px;width:520px;height:440px;transform:rotate(-4deg)"></div>
<div class="abs frame" style="left:130px;top:2180px;width:570px;height:400px">
  <div class="photo" style="left:14px;top:14px;width:542px;height:372px;background:linear-gradient(180deg,#4e6a3c 0%,#7d9657 45%,#e7d2cf 70%,#8aa35c 100%)" role="img" aria-label="Four young girls in pink dresses with flower crowns sitting on the grass"></div>
</div>
<h2 class="abs h2 contribute-title">You contribute to<br>the experience.</h2>
<p class="abs copy contribute-copy">Please refrain from wearing perfume or other strong scents to class. Turn off cell phones or make them completely silent. In other words no vibration. Remove shoes in the vestibule before entering the practice area. Be on time to class. If you intend to miss a class please email (hello@tranquilharbor.example) or TEXT: 555-014-2287</p>
<a class="abs btn" style="left:790px;top:2486px">Register For Classes</a>

<section class="abs classes"></section>
<h2 class="abs h2" style="left:86px;top:2770px">Our Classes</h2>
<p class="abs copy classes-copy">A typical part of Kundalini Yoga is a dynamic or flowing exercise series, beside quiet posture-holding exercises and versatile meditations, which are often also applied to Mantra music. The life energy is brought to flow. This can lead to greater vigor and more awareness in everyday life and a more conscious and healthy dealing with one self and others. Kundalini Yoga is not dogmatic, but impact-oriented, full of meditative elements and techniques that can be</p>
<div class="abs class-item" style="top:3030px">
  <svg width="34" height="44" viewBox="0 0 34 44"><circle cx="17" cy="6" r="5" fill="var(--accent)"/><path d="M17 12v18M6 22l11-6 11 6M4 40h26M10 36l7-6 7 6" stroke="var(--accent)" stroke-width="3" fill="none"/></svg>
  <div><h4>FlowFit Barre</h4><span>19/05/15 - 01:00pm - 03:00pm</span></div>
</div>
<div class="abs class-item" style="top:3125px">
  <svg width="34" height="44" viewBox="0 0 34 44"><circle cx="17" cy="6" r="5" fill="var(--accent)"/><path d="M17 12v18M6 22l11-6 11 6M4 40h26M10 36l7-6 7 6" stroke="var(--accent)" stroke-width="3" fill="none"/></svg>
  <div><h4>FlowFit Core</h4><span>19/05/15 - 01:00pm - 03:00pm</span></div>
</div>
<div class="abs class-item" style="top:3220px;border-bottom:none">
  <svg width="34" height="44" viewBox="0 0 34 44"><circle cx="17" cy="6" r="5" fill="var(--accent)"/><path d="M17 12v18M6 22l11-6 11 6M4 40h26M10 36l7-6 7 6" stroke="var(--accent)" stroke-width="3" fill="none"/></svg>
  <div><h4>FlowFit Core</h4><span>19/05/15 - 01:00pm - 03:00pm</span></div>
</div>
<div class="photo" style="left:617px;top:2721px;width:494px;height:619px;background:linear-gradient(180deg,#3f4a5a 0%,#c9c4c0 40%,#eeeeee 60%,#5b6b7c 100%);box-shadow:0 4px 14px rgba(0,0,0,.25)" role="img" aria-label="Teacher in white with arms raised overhead, seen from above"></div>

<section class="abs blog" role="img" aria-label="Grey misty landscape with a person meditating"></section>
<h2 class="abs h2" style="left:86px;top:3403px">Our Blog</h2>
<svg class="abs arrow" style="left:50px" width="18" height="30" viewBox="0 0 18 30"><path d="M15 3L4 15l11 12" stroke="#222" stroke-width="3" fill="none"/></svg>
<svg class="abs arrow" style="left:1132px" width="18" height="30" viewBox="0 0 18 30"><path d="M3 3l11 12L3 27" stroke="#222" stroke-width="3" fill="none"/></svg>
<article class="abs card" style="left:86px;background:var(--blue)"><h5>Contrary to popular belief, Lorem Ipsum random text.</h5><p>24 Dec, Monday @ 08:00 am</p></article>
<article class="abs card" style="left:435px;background:var(--pink)"><h5>Contrary to popular belief, Lorem Ipsum random text.</h5><p>24 Dec, Monday @ 08:00 am</p></article>
<article class="abs card" style="left:790px;background:var(--peach)"><h5>Contrary to popular belief, Lorem Ipsum random text.</h5><p>24 Dec, Monday @ 08:00 am</p></article>

<div class="abs contact"></div>
<svg class="abs" style="left:576px;top:3760px" width="48" height="48" viewBox="0 0 48 48"><circle cx="24" cy="24" r="20" fill="var(--lilac)"/></svg>
<div class="abs field" style="top:3820px">Name</div>
<div class="abs field" style="top:3863px">Email Address</div>
<div class="abs field" style="top:3906px;height:70px">Message</div>
<div class="abs submit">SUBMIT</div>

<footer class="abs footer">
  <span>© Copyright 2018 | All Rights Reserved.</span>
  <nav><span>Home</span><span>About</span><span>Events</span><span>Classes</span><span>Blog</span><span>Contact</span></nav>
</footer>

</body>
</html>
```